Presentazione aziendale Brimlet

We need a presentation like the one made in English, this time with the texts in Italian (new texts that I will provide shortly).

```html
<!DOCTYPE html>
<html lang="it">
<head>
<meta charset="utf-8">
<title>Brimlet – Presentazione aziendale</title>
<link href="https://fonts.googleapis.com/css2?family=Montserrat:wght@300;400;500;600;700;800&display=swap" rel="stylesheet">
<style>
:root{
  --navy:#0e4a70;
  --navy-deep:#0b3f61;
  --blue:#2ea3dc;
  --ink:#1f1f1f;
  --text:#3a3a3a;
  --wordmark:#5a5a5a;
  --paper:#ffffff;
}
*{margin:0;padding:0;box-sizing:border-box}
html,body{width:859px;height:1200px;overflow:hidden;background:#fff}
body{position:relative;font-family:'Montserrat',sans-serif;color:var(--text)}
.page{position:absolute;width:368px;height:284px;background:var(--paper);overflow:hidden;box-shadow:0 1px 5px rgba(0,0,0,.28)}
.page--back{left:46px;top:115px;background:linear-gradient(160deg,var(--navy) 0%,var(--navy-deep) 100%)}
.page--cover{left:451px;top:115px;background:linear-gradient(180deg,#eef1f6 0%,#f7eff4 45%,#e3e6ec 80%,#d7dbe2 100%)}
.page--profile{left:46px;top:462px}
.page--strengths{left:451px;top:462px}
.page--iot{left:231px;top:801px}

/* wordmark */
.brand{position:absolute;font-family:'Montserrat',sans-serif;font-weight:300;color:var(--wordmark);white-space:nowrap;line-height:1}

/* back cover */
.back__disc{position:absolute;left:-17px;top:192px;width:142px;height:142px;border-radius:50%;background:#fff;border:3px solid var(--blue)}
.back .brand{left:32px;top:218px;font-size:11px}
.contacts{position:absolute;left:33px;top:236px;font-size:4.4px;color:var(--ink);line-height:5.2px;list-style:none}
.contacts li{display:flex;align-items:flex-start;margin-bottom:1.6px}
.contacts svg{width:4px;height:4px;margin-right:3px;margin-top:.5px;flex:none}
.social{position:absolute;top:257px;left:294px;display:flex;gap:5px}
.social span{width:9px;height:9px;border-radius:50%;background:#fff}

/* cover */
.cover .brand{left:18px;top:76px;font-size:25px}
.cover__title{position:absolute;left:18px;top:117px;font-weight:800;font-size:22px;line-height:19px;color:var(--blue);letter-spacing:.3px}
.cover__bar{position:absolute;left:18px;top:162px;width:2px;height:24px;background:var(--blue)}
.cover__intro{position:absolute;left:24px;top:161px;width:128px;font-size:4px;line-height:5px;font-weight:500;color:var(--ink)}
.cover__frame{position:absolute;left:164px;top:28px;width:224px;height:224px;border-radius:50%;border:4px solid var(--blue);overflow:hidden}
.cover__photo{width:100%;height:100%;background:radial-gradient(circle at 40% 45%,#f3dbe6 0%,#e7c8d6 25%,#b9c8e0 48%,#3d5d8c 62%,#1c1c22 80%)}
.cover__url{position:absolute;left:18px;top:266px;font-size:7px;font-weight:700;color:var(--ink)}
.cover__rule{position:absolute;left:75px;top:271px;width:293px;height:.6px;background:#7a8fa8}

/* inner pages */
.section-bar{position:absolute;left:0;width:24px;height:6px;background:var(--blue)}
.section-title{position:absolute;left:28px;font-size:6.6px;font-weight:700;color:var(--blue);letter-spacing:.1px;line-height:8px}
.copy{position:absolute;font-size:3.3px;line-height:4.3px;color:var(--ink)}
.copy p{margin-bottom:2.8px}
.photo-frame{position:absolute;background:var(--blue)}
.photo{position:absolute}
.footer .brand{left:27px;top:264px;font-size:11.5px}
.footer__rule{position:absolute;left:82px;top:273px;width:219px;height:.7px;background:#444}
.footer__url{position:absolute;left:305px;top:269px;font-size:6px;font-weight:700;color:var(--ink)}

.page--profile .section-bar{top:36px}
.page--profile .section-title{top:35px}
.page--profile .copy{left:28px;top:54px;width:148px}
.page--profile .photo-frame{left:191px;top:49px;width:117px;height:178px}
.page--profile .photo{left:196px;top:53px;width:172px;height:170px;background:linear-gradient(120deg,#e9e4dc 0%,#c9b8a8 35%,#8a4048 55%,#a9c6dc 80%,#e8e6e2 100%)}

.page--strengths .section-bar{top:82px}
.page--strengths .section-title{top:81px}
.page--strengths .copy{left:28px;width:148px}
.strengths__intro{top:98px}
.strengths__more{top:153px}
.bullets{position:absolute;left:28px;top:108px;list-style:none;font-size:5.4px;color:var(--ink)}
.bullets li{display:flex;align-items:center;height:14.5px}
.bullets svg{width:5px;height:5px;margin-right:4px}
.page--strengths .photo-frame{left:191px;top:49px;width:117px;height:178px}
.page--strengths .photo{left:196px;top:53px;width:172px;height:170px;background:linear-gradient(180deg,#1e2430 0%,#2b3444 40%,#31549a 70%,#c9a58f 88%,#1d2330 100%)}

.page--iot .photo{left:0;top:0;width:368px;height:166px;background:linear-gradient(180deg,#e9b3d6 0%,#c6a3d4 35%,#8a8fc6 62%,#4f5f93 85%,#3b4c7c 100%)}
.page--iot .section-bar{top:178px}
.page--iot .section-title{top:177px}
.page--iot .copy{left:28px;top:194px;width:316px}
</style>
</head>
<body>

<section class="page page--back back">
  <div class="back__disc"></div>
  <div class="brand">Brimlet</div>
  <ul class="contacts">
    <li><svg viewBox="0 0 10 10"><path d="M5 0.5a3.2 3.2 0 0 0-3.2 3.2C1.8 6 5 9.5 5 9.5S8.2 6 8.2 3.7A3.2 3.2 0 0 0 5 .5z" fill="#2ea3dc"/><circle cx="5" cy="3.7" r="1.2" fill="#fff"/></svg><span>Via dei Tigli 14/B<br>35121 Padova</span></li>
    <li><svg viewBox="0 0 10 10"><path d="M2.2 1l1.8 1.9-1 1.3c.6 1.3 1.6 2.3 2.9 2.9l1.3-1L9 7.9 7.9 9C4.3 8.8 1.2 5.7 1 2.1z" fill="#2ea3dc"/></svg><span>+39 049.5550172</span></li>
    <li><svg viewBox="0 0 10 10"><rect x="0.8" y="2" width="8.4" height="6" fill="#2ea3dc"/><path d="M.8 2l4.2 3.4L9.2 2" fill="none" stroke="#fff" stroke-width=".8"/></svg><span>info@brimlet.it</span></li>
  </ul>
  <div class="social"><span></span><span></span><span></span></div>
</section>

<section class="page page--cover cover">
  <div class="brand">Brimlet</div>
  <h1 class="cover__title">SOFTWARE<br>FACTORY</h1>
  <div class="cover__bar"></div>
  <p class="cover__intro">Una software factory si distingue per la capacità di gestire l'intero ciclo di vita dello sviluppo del software. Brimlet Srl nasce nel 2005 proprio con lo scopo di produrre software specialistico, sviluppato con tecnologia e metodologia "allo stato dell'arte" e standard qualitativi e di sicurezza elevati.</p>
  <div class="cover__frame"><div class="cover__photo" role="img" aria-label="Mano che tocca un tablet con grafici e interfacce digitali"></div></div>
  <div class="cover__url">www.brimlet.it</div>
  <div class="cover__rule"></div>
</section>

<section class="page page--profile">
  <div class="section-bar"></div>
  <h2 class="section-title">PROFILO DELLA SOCIETÀ</h2>
  <div class="copy">
    <p>Brimlet Srl è una software house italiana nata con lo scopo di produrre software specialistico, sviluppato con tecnologia e metodologia allo stato dell'arte.</p>
    <p>Brimlet ha una comprovata esperienza nell'operare con organizzazioni di ogni dimensione, anche complesse, e con forniture di larga scala, sia per realtà locali sia per gruppi internazionali che la scelgono come fornitore del proprio software principale.</p>
    <p>Siamo stati selezionati per progetti pubblici di ricerca e sviluppo di grande valore e siamo diventati fornitori di sistemi informativi per eventi internazionali, affermandoci accanto ai principali operatori del settore dopo attente selezioni.</p>
    <p>Un ente universitario ha certificato la qualità del software Brimlet, adottato in un grande evento internazionale, e i tecnici che lo hanno valutato lo hanno definito un'eccellenza italiana.</p>
    <p>L'asset management di Brimlet nasce da una stretta sinergia con aziende e professionisti, offrendo soluzioni a 360°, dall'analisi allo sviluppo, nel settore pubblico e privato, restando sempre competitiva sul piano economico.</p>
    <p>Seguendo questa logica Brimlet è entrata a far parte di un gruppo di aziende del settore.</p>
    <p>Il gruppo, nato negli anni 80 come software house specializzata nell'elaborazione delle paghe, è diventato in poco tempo un punto di riferimento nel mercato delle soluzioni per le risorse umane.</p>
    <p>L'ingresso di Brimlet rafforza l'offerta del gruppo, con l'obiettivo di diventare un riferimento per lo sviluppo di applicativi integrati per tutte le aree aziendali: risorse umane, finanza, IT, logistica, produzione, vendita.</p>
    <p>Forte del suo know-how, Brimlet propone anche una serie di prodotti di cui detiene la completa titolarità del codice, con soluzioni verticali facilmente integrabili con i sistemi già presenti sul mercato.</p>
  </div>
  <div class="photo-frame"></div>
  <div class="photo" role="img" aria-label="Team di sviluppatori al lavoro davanti a un monitor con codice"></div>
  <footer class="footer">
    <div class="brand">Brimlet</div>
    <div class="footer__rule"></div>
    <div class="footer__url">www.brimlet.it</div>
  </footer>
</section>

<section class="page page--strengths">
  <div class="section-bar"></div>
  <h2 class="section-title">PUNTI DI FORZA</h2>
  <p class="copy strengths__intro">Tra i vari ambiti in cui Brimlet ha una consolidata esperienza, il suo know-how è distintivo soprattutto nei seguenti settori:</p>
  <ul class="bullets">
    <li><svg viewBox="0 0 10 10"><circle cx="5" cy="5" r="5" fill="#2ea3dc"/><path d="M2.8 5.1l1.5 1.5 2.9-3" fill="none" stroke="#fff" stroke-width="1.2"/></svg>I.O.T. (Internet of Things)</li>
    <li><svg viewBox="0 0 10 10"><circle cx="5" cy="5" r="5" fill="#2ea3dc"/><path d="M2.8 5.1l1.5 1.5 2.9-3" fill="none" stroke="#fff" stroke-width="1.2"/></svg>Digital Transformation</li>
    <li><svg viewBox="0 0 10 10"><circle cx="5" cy="5" r="5" fill="#2ea3dc"/><path d="M2.8 5.1l1.5 1.5 2.9-3" fill="none" stroke="#fff" stroke-width="1.2"/></svg>Meeting Incentive, Conference &amp; Exhibition</li>
  </ul>
  <div class="copy strengths__more">
    <p>La natura dei prodotti Brimlet è enterprise, fortemente orientata al cloud, con comprovata robustezza, prestazioni e scalabilità.</p>
    <p>Tutti i prodotti sono utilizzabili via web, anche in mobilità tramite smartphone e tablet.</p>
    <p>I numerosi progetti realizzati hanno permesso a Brimlet di creare pacchetti applicativi pronti all'uso. Di seguito alcune delle nostre principali realizzazioni.</p>
  </div>
  <div class="photo-frame"></div>
  <div class="photo" role="img" aria-label="Uomo in giacca che regge un tablet con una mappa del mondo e una rete di contatti"></div>
  <footer class="footer">
    <div class="brand">Brimlet</div>
    <div class="footer__rule"></div>
    <div class="footer__url">www.brimlet.it</div>
  </footer>
</section>

<section class="page page--iot">
  <div class="photo" role="img" aria-label="Skyline di una città al tramonto con icone di cloud e connessioni wireless"></div>
  <div class="section-bar"></div>
  <h2 class="section-title">I.O.T. (INTERNET OF THINGS)</h2>
  <div class="copy">
    <p>Brimlet ha nel suo portafoglio una serie di soluzioni verticali dedicate all'industria 4.0, alla sanità e al controllo accessi.</p>
    <p>Le soluzioni Internet of Things di Brimlet permettono di acquisire e analizzare i dati di dispositivi, persone e luoghi connessi per fornire informazioni utili in ogni tipo di ambiente: industriale, commerciale, sanitario o residenziale.</p>
    <p>Nodo.Core è la piattaforma di Brimlet interamente in cloud, basata su microservizi e dedicata all'IoT, capace di dare risposte concrete con pieno supporto alle tecnologie emergenti in ogni settore.</p>
    <p>È una piattaforma progettata per gestire da remoto, in modo centralizzato, le più diverse tipologie di dispositivi intelligenti nella domotica, nella mobilità e nel controllo accessi di spazi collettivi.</p>
    <p>Dagli sviluppi sono nati prodotti specifici, tra cui Nodo.Care, per la sanità, e Nodo.Gate, per il controllo accessi.</p>
  </div>
  <footer class="footer">
    <div class="brand">Brimlet</div>
    <div class="footer__rule"></div>
    <div class="footer__url">www.brimlet.it</div>
  </footer>
</section>

</body>
</html>
```